Package Design for Chew Bone Guild for Rivora

Would like a label to put on a 6x9 package.

Here is my site: chewboneguild.example

Here are the labels I like:
https://tomandhound.example/collections/chews/products/6-inch-basic-chews
https://www.rivora.example/stores/Tom+%26+Hound/page/A1D23456-7ABC-42EF-9D01-123456789ABC?ref_=xyz_qrs
https://quiet-meadowland.example/amber-paw-mini-chews-6-25-pack/
https://www.fernandkettle.example/shop/open-trail-chew-rods

```html
<!DOCTYPE html>
<html lang="en">
<head>
<meta charset="utf-8">
<title>Chew Bone Guild – Bully Sticks Pouch Label</title>
<link rel="stylesheet" href="https://fonts.googleapis.com/css2?family=Fredoka:wght@500;600;700&display=swap">
<style>
  :root {
    --page-bg: #f4f5f3;
    --pouch-white: #fbfbfb;
    --leaf-green: #6cc24a;
    --leaf-green-light: #a6dd8c;
    --sky-blue: #5bc3dc;
    --sky-blue-light: #9fdcec;
    --chew-brown: #8a4a2a;
    --chew-brown-dark: #5e2f18;
    --ink: #1d1d1d;
    --white: #ffffff;
    --photo-gold: #d9b27a;
    --photo-cream: #f1e3c9;
  }
  * { box-sizing: border-box; margin: 0; padding: 0; }
  html, body {
    width: 1200px; height: 835px; overflow: hidden;
    background: var(--page-bg);
    font-family: "Fredoka", sans-serif;
  }
  .canvas {
    position: relative; width: 1200px; height: 835px;
  }
  .label {
    position: absolute; left: 435px; top: 138px;
    width: 330px; height: 560px;
    background: var(--pouch-white);
    overflow: hidden;
    border-radius: 10px 10px 4px 4px;
    box-shadow: 0 10px 30px rgba(0,0,0,.08);
  }
  .label__top-strip {
    position: absolute; left: 0; top: 0; width: 100%; height: 16px;
    background: var(--leaf-green);
  }
  .brand-seal {
    position: absolute; left: 50%; top: 32px; transform: translateX(-50%);
    width: 112px; height: 112px; border-radius: 50%;
    border: 3px solid var(--ink);
    display: flex; align-items: center; justify-content: center;
    text-align: center;
  }
  .brand-seal__name {
    font-weight: 700; font-size: 15px; line-height: 1.1;
    color: var(--ink); letter-spacing: .5px;
  }
  .hero-photo {
    position: absolute; left: 70px; top: 168px; width: 186px; height: 160px;
    border-radius: 90px 90px 0 0;
    background: radial-gradient(ellipse at 50% 45%, var(--photo-cream) 0%, var(--photo-gold) 60%, #c49356 100%);
  }
  .chew-band {
    position: absolute; left: 16px; top: 322px; width: 298px; height: 46px;
    background: linear-gradient(180deg, var(--chew-brown) 0%, #a35b34 45%, var(--chew-brown-dark) 100%);
  }
  .green-panel {
    position: absolute; left: 16px; top: 368px; width: 298px; height: 192px;
    background: linear-gradient(90deg, var(--leaf-green) 0%, #7fcc5e 55%, var(--leaf-green-light) 100%);
  }
  .product-title {
    position: absolute; left: 0; top: 378px; width: 100%;
    text-align: center; color: var(--white); font-weight: 700;
    line-height: .95;
  }
  .product-title__line1 {
    font-size: 38px; display: flex; align-items: center; justify-content: center; gap: 8px;
  }
  .product-title__dot {
    width: 9px; height: 9px; border-radius: 50%; background: var(--white);
  }
  .product-title__line2 { font-size: 50px; letter-spacing: 1px; }
  .pack-pill {
    position: absolute; left: 44px; top: 455px; width: 226px; height: 28px;
    border-radius: 14px;
    background: linear-gradient(90deg, var(--sky-blue) 0%, var(--sky-blue-light) 100%);
    transform: rotate(-1.5deg);
    color: var(--white); font-weight: 600; font-size: 12.5px;
    display: flex; align-items: center; justify-content: center;
  }
  .benefits {
    position: absolute; left: 52px; top: 496px; width: 250px;
    display: grid; grid-template-columns: 96px 1fr; row-gap: 9px; column-gap: 6px;
    list-style: none;
  }
  .benefit {
    display: flex; align-items: center; gap: 6px;
    color: var(--white); font-weight: 600; font-size: 8px; white-space: nowrap;
  }
  .benefit__icon {
    width: 16px; height: 16px; border-radius: 50%;
    background: var(--white); flex: none;
    display: flex; align-items: center; justify-content: center;
  }
</style>
</head>
<body>
<main class="canvas">
  <section class="label">
    <div class="label__top-strip"></div>

    <div class="brand-seal">
      <span class="brand-seal__name">Chew Bone<br>Guild</span>
    </div>

    <div class="hero-photo" role="img" aria-label="Photo of a smiling golden retriever looking over the chew"></div>
    <div class="chew-band" role="img" aria-label="Close-up photo of a bully stick laid horizontally"></div>

    <div class="green-panel"></div>

    <h1 class="product-title">
      <span class="product-title__line1"><span class="product-title__dot"></span>BULLY<span class="product-title__dot"></span></span>
      <span class="product-title__line2">STICKS</span>
    </h1>

    <p class="pack-pill">24 PACK All Natural Bully Sticks</p>

    <ul class="benefits">
      <li class="benefit">
        <span class="benefit__icon"><svg width="10" height="10" viewBox="0 0 10 10"><path d="M5 9V2M5 9L2 4M5 9l3-5" stroke="#6cc24a" stroke-width="1.2" fill="none" stroke-linecap="round"/></svg></span>
        Grass-Fed Beef
      </li>
      <li class="benefit">
        <span class="benefit__icon"><svg width="10" height="10" viewBox="0 0 10 10"><path d="M2 2.5c1-1 2-.5 3 0 1-.5 2-1 3 0 .6 1 0 2.5-.4 3.5L7 9 5.8 6.5 5 6l-.8.5L3 9l-.6-3C2 5 1.4 3.5 2 2.5z" stroke="#8aa" stroke-width=".8" fill="none"/></svg></span>
        Ideal for Dental Health
      </li>
      <li class="benefit">
        <span class="benefit__icon"><svg width="10" height="10" viewBox="0 0 10 10"><circle cx="5" cy="4" r="2.3" stroke="#c8902c" stroke-width="1" fill="none"/><path d="M3.8 6l-1 3 2.2-1 2.2 1-1-3" stroke="#c8902c" stroke-width=".9" fill="none"/></svg></span>
        Premium Quality
      </li>
      <li class="benefit">
        <span class="benefit__icon"><svg width="10" height="10" viewBox="0 0 10 10"><ellipse cx="5" cy="5" rx="3.6" ry="2.8" fill="#d9504f"/><circle cx="6" cy="4.6" r="1" fill="#fff"/></svg></span>
        High in Protein
      </li>
    </ul>
  </section>
</main>
</body>
</html>
```